WeatheredIt.net wordpress design

Concept: Website where personal stories, personal videos can be posted as a challenge while awaiting the wisdom of experience from others who have Weathered It same event or challenge in their lifetime.
Support aspects will be in 4 quadrants of Challenges:
1. Financial 2. Medical & Physical
3. Legal Matters 4. Psychological & Spiritual - ability to chat online with a spiritual/psychological counselor or life coach
Updates
Wanted to thank all of you for your designs! Greatly appreciated. Very creative ideas that captured the essence of this website. Will be back with a selection very shortly.
Target Market(s)
Anyone looking for a solution based upon experiential wisdom
Industry/Entity Type
Financial
Requirements
Must have
- Interactive website: Where you can post a challenge or issue via a written question or a video and ask for a solution.
Ability to access any of the 4 Quadrants (as listed above) to ask for an expert, via experience, advice and wisdom from those who have similar challenges.

```html
<!DOCTYPE html>
<html lang="en">
<head>
<meta charset="utf-8">
<title>WeatheredIt.net</title>
<link rel="stylesheet" href="https://fonts.googleapis.com/css2?family=Old+Standard+TT:ital,wght@0,400;0,700;1,400&display=swap">
<style>
  :root{
    --gold:#f0c24a;
    --gold-soft:#f2cc7a;
    --gold-text:#d9a030;
    --orange:#f7a93a;
    --ink:#111;
    --muted:#6a6a6a;
    --grey-circle:#a9a9a9;
    --card:#efefef;
    --card-line:#cfcfcf;
    --panel-top:#efefef;
    --panel-bottom:#e0e0e0;
    --footer:#5a5a5a;
    --white:#fff;
  }
  *{box-sizing:border-box;margin:0;padding:0}
  html,body{width:1000px;height:1200px;overflow:hidden;background:var(--white)}
  body{position:relative;font-family:"Old Standard TT",Georgia,serif;color:var(--ink)}
  .abs{position:absolute}

  /* header */
  .brand-mark{left:16px;top:17px;width:158px;height:158px;border-radius:14px;background:linear-gradient(135deg,#fbc04a,var(--orange))}
  .brand-name{left:186px;top:28px;width:230px;font-size:46px;line-height:50px;color:#555}
  .brand-tagline{left:193px;top:135px;font-size:16px;color:#888;letter-spacing:.5px;border-top:1px solid #e6d3a6;padding-top:2px;width:212px}
  .account-links{left:818px;top:15px;font-size:16px}
  .help-title{left:443px;top:56px;font-size:25px;letter-spacing:.5px;font-weight:400}
  .search{left:440px;top:92px;width:326px;height:41px;border:1px solid #ddd;border-radius:6px;background:var(--white);overflow:hidden}
  .search-button{position:absolute;right:0;top:0;width:49px;height:100%;background:#eee;display:flex;align-items:center;justify-content:center}
  .search-caption{left:445px;top:141px;font-size:15px}
  .live-help{left:796px;top:104px;height:28px;width:196px;background:#e2b43d;font-size:23px;line-height:28px;color:#333;text-align:center}
  .chat-now{left:876px;top:137px;font-size:15px;display:flex;align-items:center;gap:6px}
  .chevrons{font-size:12px}

  /* categories */
  .category-band{left:0;top:193px;width:1000px;height:32px;background:linear-gradient(#f3c95a,var(--gold));z-index:2}
  .video-band{left:0;top:268px;width:1000px;height:126px;background:var(--gold-soft)}
  .category-circle{top:176px;width:84px;height:84px;border-radius:50%;background:var(--grey-circle);z-index:1}
  .category-label{top:193px;width:240px;text-align:center;color:var(--white);font-size:25px;letter-spacing:.5px;line-height:32px;z-index:3}
  .category-icon{top:226px;width:30px;height:30px;z-index:3}
  .card{top:246px;width:214px;height:218px;background:var(--card);border:1px solid var(--card-line)}
  .card-video{position:absolute;left:6px;top:21px;width:200px;height:124px;border:2px solid #111;border-top:0;border-left:0}
  .card-time{position:absolute;right:6px;top:4px;background:#555;color:#fff;font:bold 9px Arial,sans-serif;padding:3px 5px;border-radius:8px}
  .card-title{position:absolute;left:6px;top:148px;font-size:18px;color:var(--gold-text);font-weight:400}
  .card-text{position:absolute;left:8px;top:170px;font-size:14px;line-height:19px;width:200px}
  .card-more{position:absolute;right:5px;bottom:0;font-size:18px;color:#444}

  /* section buttons */
  .section-button{left:41px;width:174px;height:35px;border:1px solid #d9ad45;border-radius:6px;background:linear-gradient(#f7d77c,#eebf55);text-align:center;font-size:22px;line-height:34px;letter-spacing:.5px}
  .section-note{font-size:14px;color:var(--muted)}
  .rule{left:20px;width:960px;height:1px;background:linear-gradient(90deg,transparent,#e5e5e5 15%,#e5e5e5 85%,transparent)}

  /* review */
  .review-glow{left:120px;top:536px;width:760px;height:175px;background:radial-gradient(ellipse at center,#fbdf9c 0%,#fdf0cf 45%,rgba(255,255,255,0) 72%)}
  .review-box{left:198px;top:541px;width:622px;height:166px;border:1px solid #d2d2d2;border-radius:12px;background:#e7e7e7}
  .review-photo{left:216px;top:548px;width:136px;height:148px;background:linear-gradient(#e8e8e8,#c9c5bf)}
  .review-quote{left:360px;top:546px;width:455px;font-size:27px;font-style:italic;line-height:34px}
  .review-author{left:577px;top:678px;font-size:23px;font-style:italic}
  .review-arrow{top:598px}

  /* questions */
  .question-panel{left:36px;top:779px;width:927px;height:314px;border:1px solid #d4d4d4;border-radius:8px;background:linear-gradient(var(--panel-top),var(--panel-bottom))}
  .panel-title{top:782px;font-size:25px;letter-spacing:.5px;font-weight:400}
  .question-list{left:49px;top:817px;width:505px;list-style:none}
  .question{height:28px;margin-bottom:8.4px;background:var(--white);display:flex;align-items:center;font-size:14.5px;padding-left:2px}
  .question::before{content:"";border-left:6px solid #999;border-top:5px solid transparent;border-bottom:5px solid transparent;margin-right:3px}
  .question-topic{color:var(--gold-text);margin-right:5px}
  .question-link{margin-left:auto;margin-right:6px;font-size:12px;font-style:italic;color:#999}
  .mode-tab{top:788px;width:46px;height:20px;font-size:13px;font-style:italic;text-align:center;line-height:20px}
  .mode-video{left:843px;background:#b3b3b3}
  .mode-post{left:894px;background:var(--gold)}
  .field{left:593px;width:352px;background:var(--white);font-size:16px;padding:3px 7px}
  .submit{left:888px;top:1039px;background:#e3e3e3;font-size:13px;font-style:italic;padding:1px 4px;color:#444}

  /* footer */
  .footer{left:0;top:1140px;width:1000px;height:60px;background:var(--footer);color:var(--white);font-size:14.5px;display:flex;align-items:center;padding-left:27px;gap:24px}
</style>
</head>
<body>

<header>
  <div class="abs brand-mark"></div>
  <div class="abs brand-name">Weathered It</div>
  <div class="abs brand-tagline">wisdom from all of us</div>
  <nav class="abs account-links">register | log in | help</nav>
  <h2 class="abs help-title">GET HELP NOW!</h2>
  <div class="abs search">
    <div class="search-button">
      <svg width="26" height="26" viewBox="0 0 26 26"><circle cx="10" cy="10" r="7.5" fill="none" stroke="#111" stroke-width="3"/><line x1="15.5" y1="15.5" x2="23" y2="23" stroke="#111" stroke-width="4" stroke-linecap="round"/></svg>
    </div>
  </div>
  <p class="abs search-caption">Lorem ipsum dolor sit amet, consectetur adipisc.</p>
  <div class="abs live-help">Get live help now!</div>
  <div class="abs chat-now">
    <svg width="26" height="22" viewBox="0 0 26 22"><rect x="7" y="1" width="17" height="12" fill="#fff" stroke="#777"/><rect x="1" y="6" width="17" height="11" fill="#fff" stroke="#777"/><path d="M4 17 L4 21 L8 17" fill="#fff" stroke="#777"/></svg>
    <span>chat now <span class="chevrons">&gt;&gt;</span></span>
  </div>
</header>

<section class="categories">
  <div class="abs video-band"></div>

  <div class="abs category-circle" style="left:101px"></div>
  <div class="abs category-circle" style="left:340px"></div>
  <div class="abs category-circle" style="left:576px"></div>
  <div class="abs category-circle" style="left:812px"></div>
  <div class="abs category-band"></div>

  <div class="abs category-label" style="left:23px">HEALTH</div>
  <div class="abs category-label" style="left:263px">ECONOMIC</div>
  <div class="abs category-label" style="left:498px">LEGAL</div>
  <div class="abs category-label" style="left:737px">SPIRITUAL</div>

  <svg class="abs category-icon" style="left:128px" viewBox="0 0 30 30"><path d="M11 2h8v9h9v8h-9v9h-8v-9H2v-8h9z" fill="#111"/></svg>
  <svg class="abs category-icon" style="left:367px" viewBox="0 0 30 30"><text x="15" y="26" text-anchor="middle" font-family="Arial,sans-serif" font-weight="bold" font-size="28" fill="#111">$</text></svg>
  <svg class="abs category-icon" style="left:603px" viewBox="0 0 30 30" fill="none" stroke="#111" stroke-width="2"><line x1="15" y1="3" x2="15" y2="26"/><line x1="4" y1="7" x2="26" y2="7"/><line x1="9" y1="27" x2="21" y2="27"/><path d="M4 7 L1 17 H8 Z M26 7 L23 17 H29 Z" fill="#111"/></svg>
  <svg class="abs category-icon" style="left:839px" viewBox="0 0 30 30"><path d="M16 2 C22 10 21 16 18 21 C17 24 14 27 11 28 C14 24 13 20 11 17 C11 22 9 23 9 23 C9 17 12 12 16 2Z" fill="#111"/></svg>

  <article class="abs card" style="left:39px">
    <div class="card-video" role="img" aria-label="Health story video: a presenter speaking in front of a wall" style="background:linear-gradient(135deg,#6f625a,#2c2a2e)"><span class="card-time">00:00</span></div>
    <h3 class="card-title">Lore ipsum</h3>
    <p class="card-text">Lorem ipsum dolor sit amet, consectetur adipiscing elit.</p>
    <span class="card-more">+</span>
  </article>
  <article class="abs card" style="left:275px">
    <div class="card-video" role="img" aria-label="Economic story video: a man writing a plan on a whiteboard" style="background:linear-gradient(135deg,#d8dde0,#5a5b5e)"><span class="card-time">00:00</span></div>
    <h3 class="card-title">Lore ipsum</h3>
    <p class="card-text">Lorem ipsum dolor sit amet, consectetur adipiscing elit.</p>
    <span class="card-more">+</span>
  </article>
  <article class="abs card" style="left:510px">
    <div class="card-video" role="img" aria-label="Legal story video: a lawyer giving an interview" style="background:linear-gradient(135deg,#3b4a78,#2a2a34 60%,#8a2a3a)"><span class="card-time">00:00</span></div>
    <h3 class="card-title">Lore ipsum</h3>
    <p class="card-text">Lorem ipsum dolor sit amet, consectetur adipiscing elit.</p>
    <span class="card-more">+</span>
  </article>
  <article class="abs card" style="left:747px">
    <div class="card-video" role="img" aria-label="Spiritual story video: a speaker at a candlelit gathering" style="background:linear-gradient(135deg,#2a2222,#5a4a44 60%,#1a1616)"><span class="card-time">00:00</span></div>
    <h3 class="card-title">Lore ipsum</h3>
    <p class="card-text">Lorem ipsum dolor sit amet, consectetur adipiscing elit.</p>
    <span class="card-more">+</span>
  </article>
</section>

<section class="reviews">
  <div class="abs section-button" style="top:489px">REVIEWS</div>
  <p class="abs section-note" style="left:234px;top:499px">Lorem ipsum dolor sit amet, consectetur adipiscing elit quisque venenatis euismod neque ac fringilla.</p>
  <div class="abs rule" style="top:535px"></div>
  <div class="abs review-glow"></div>
  <svg class="abs review-arrow" style="left:146px" width="24" height="42" viewBox="0 0 24 42"><path d="M21 2 L3 21 L21 40" fill="none" stroke="#ccc" stroke-width="3"/></svg>
  <svg class="abs review-arrow" style="left:848px" width="24" height="42" viewBox="0 0 24 42"><path d="M3 2 L21 21 L3 40" fill="none" stroke="#ccc" stroke-width="3"/></svg>
  <div class="abs review-box"></div>
  <div class="abs review-photo" role="img" aria-label="Portrait of the reviewer"></div>
  <blockquote class="abs review-quote">“Thanks to, Weathered It i managed to be happy again after my wife died, thanks to them i can have again a life!”</blockquote>
  <cite class="abs review-author">Harold Benning.</cite>
  <div class="abs rule" style="top:711px"></div>
</section>

<section class="get-help">
  <div class="abs section-button" style="top:723px">GET HELP!</div>
  <p class="abs section-note" style="left:236px;top:734px">Lorem ipsum dolor sit amet, consectetur adipiscing elit quisque venenatis euismod neque ac fringilla.</p>
  <div class="abs rule" style="top:768px"></div>

  <div class="abs question-panel"></div>
  <h2 class="abs panel-title" style="left:48px">LATEST QUESTIONS</h2>
  <ul class="abs question-list">
    <li class="question"><span class="question-topic">&nbsp;LEGAL :</span>Worried about divorce laws in California help!...<span class="question-link">check it! &gt;&gt;</span></li>
    <li class="question"><span class="question-topic">HEALTH :</span>Wounded leg, pictures added...<span class="question-link">check it! &gt;&gt;</span></li>
    <li class="question"><span class="question-topic">LEGAL :</span>How to select a good lawyer?...<span class="question-link">check it! &gt;&gt;</span></li>
    <li class="question"><span class="question-topic">SPIRITUAL :</span>I think im losing my faith in god...<span class="question-link">check it! &gt;&gt;</span></li>
    <li class="question"><span class="question-topic">ECONOMIC :</span>Need help to fix house earnings...<span class="question-link">check it! &gt;&gt;</span></li>
    <li class="question"><span class="question-topic">&nbsp;LEGAL :</span>Is this legal?...<span class="question-link">check it! &gt;&gt;</span></li>
    <li class="question"><span class="question-topic">&nbsp;LEGAL :</span>Arrested for drinking alcohol, suggestions...<span class="question-link">check it! &gt;&gt;</span></li>
  </ul>

  <h2 class="abs panel-title" style="left:592px">POST QUESTION</h2>
  <div class="abs mode-tab mode-video">video</div>
  <div class="abs mode-tab mode-post">post</div>
  <div class="abs field" style="top:817px;height:25px">Tittle</div>
  <div class="abs field" style="top:855px;height:210px;padding-top:5px">Write here your answer.</div>
  <div class="abs submit">submit</div>
</section>

<footer class="abs footer">
  <span>All rights reserved Weathered It.</span>
  <span>Site Map | help | Rights | Lore | Ipsum | Dolor</span>
  <span>Lorem ipsum dolor sit amet, consectetur adipiscing elit.</span>
</footer>

</body>
</html>
```